UX design for mobile app and responsive website

The website will publish completed jobs from local trade contractors, such as plumbers, electricians, gardeners, etc.

There should be pages for: the job, a list of jobs that can be refined by area and job category, business with details of the business and their jobs.

The website should be responsive.

The mobile app is for the businesses to register and upload the jobs, including optional photos. They can also edit or delete jobs.

Wire frames and logo are attached.

Target Market(s)

Trades contractors. Plumbers, electricians, builders, painters, etc.

Coding

Coded - Design and coding required

Number of Pages Required

5+ page

Font styles to use
Sans Serif

Colors
33a6d7
0492cd
85cae6
3377b5
85acd3

Requirements
Must have
• Responsive website.
• Job page, job list page, business page.

```html
<!DOCTYPE html>
<html lang="en">
<head>
<meta charset="utf-8">
<title>TradeLog – Browse work from the best local tradies</title>
<link rel="stylesheet" href="https://fonts.googleapis.com/css2?family=Roboto:wght@400;500;700;900&display=swap">
<style>
  :root{
    --blue:#0492cd;
    --blue-mid:#33a6d7;
    --blue-soft:#85cae6;
    --blue-deep:#3377b5;
    --blue-muted:#85acd3;
    --ink:#1d1d1f;
    --text:#333;
    --grey-bg:#f1f1f1;
    --placeholder:#8a8a8a;
    --white:#fff;
  }
  *{box-sizing:border-box;margin:0;padding:0}
  html,body{width:675px;height:1200px;overflow:hidden}
  body{font-family:"Roboto",Arial,sans-serif;color:var(--text);background:var(--white);position:relative}

  .site-header{position:absolute;top:0;left:0;width:675px;height:40px;background:var(--white);display:flex;align-items:center;padding:0 14px 0 76px;z-index:2}
  .brand{display:flex;align-items:center;gap:6px;font-weight:900;font-size:16px;color:var(--blue);letter-spacing:.5px}
  .brand-mark{width:10px;height:10px;background:var(--blue)}
  .main-nav{display:flex;gap:16px;margin-left:auto;margin-right:14px}
  .main-nav a{font-size:8.5px;font-weight:700;color:var(--ink);text-decoration:none}
  .btn-pill{font-size:7px;font-weight:700;border-radius:10px;padding:5px 11px;margin-left:6px;text-decoration:none}
  .btn-login{background:var(--blue);color:var(--white)}
  .btn-register{border:1px solid var(--blue);color:var(--blue)}

  .hero{position:absolute;top:40px;left:0;width:675px;height:365px;background:linear-gradient(110deg,#cfc7bb 0%,#a7a39a 30%,#6f7d87 55%,#2f4f7a 80%,#263f66 100%)}

  .search-panel{position:absolute;top:162px;left:150px;width:372px;height:153px;background:rgba(4,146,205,.92);text-align:center;color:var(--white);padding-top:15px}
  .search-title{font-size:13px;font-weight:500;letter-spacing:.3px}
  .search-count{font-size:11px;font-weight:700;margin-top:4px}
  .search-fields{display:grid;grid-template-columns:1fr 1fr;gap:10px 12px;padding:14px 28px 0}
  .select{background:var(--white);height:20px;border-radius:2px;font-size:7px;color:#555;display:flex;align-items:center;justify-content:space-between;padding:0 8px;text-align:left}
  .select svg{width:7px;height:5px}
  .go-btn{position:absolute;left:50%;bottom:-16px;transform:translateX(-50%);width:32px;height:32px;border-radius:50%;background:var(--blue);border:3px solid var(--white);color:var(--white);font-weight:700;font-size:11px;display:flex;align-items:center;justify-content:center}

  .app-promo{position:absolute;top:405px;left:0;width:675px;height:157px;text-align:center}
  .section-title{font-size:23px;font-weight:700;color:var(--ink);letter-spacing:.3px}
  .app-promo .section-title{margin-top:9px}
  .app-promo p{font-size:11px;color:#444;margin-top:8px}
  .store-badges{display:flex;justify-content:center;gap:14px;margin-top:16px}
  .store-badge{width:108px;height:34px;background:#111;border-radius:6px}

  .latest-jobs{position:absolute;top:562px;left:0;width:675px;height:522px;background:var(--grey-bg);text-align:center}
  .latest-jobs .section-title{margin-top:47px}
  .job-list{position:absolute;top:106px;left:68px;width:535px;display:flex;flex-direction:column;gap:18px}
  .job-card{height:104px;background:var(--white);border:1px solid #ddd;display:flex;align-items:center;padding:0 16px 0 14px;text-align:left}
  .job-info{flex:1}
  .job-title{font-size:12px;color:var(--ink);line-height:1.3;max-width:220px}
  .job-date{font-size:6.5px;color:var(--blue);margin-top:6px;display:flex;align-items:center;gap:3px}
  .job-by{display:flex;align-items:center;gap:5px;margin-top:6px;font-size:6px;color:#555;line-height:1.3}
  .job-by .avatar{width:13px;height:13px;border-radius:50%;background:var(--blue-mid)}
  .job-images{display:flex;gap:9px}
  .image-slot{width:86px;height:78px;background:var(--placeholder);color:var(--white);font-size:7.5px;font-weight:700;display:flex;align-items:center;justify-content:center;text-align:center;line-height:1.4}

  .site-footer{position:absolute;top:1084px;left:0;width:675px;height:116px;background:var(--blue);color:var(--white);text-align:center}
  .footer-links{font-size:7.5px;margin-top:27px}
  .footer-links span{margin:0 4px}
  .copyright{font-size:6.5px;margin-top:10px}
  .social{display:flex;justify-content:center;gap:10px;margin-top:11px}
  .social span{width:13px;height:13px;background:var(--white);border-radius:2px}
  .to-top{position:absolute;right:18px;bottom:20px;width:8px;height:6px}
</style>
</head>
<body>
  <header class="site-header">
    <div class="brand"><span class="brand-mark"></span>TRADELOG</div>
    <nav class="main-nav">
      <a href="#">HOME</a><a href="#">ABOUT</a><a href="#">JOBS</a><a href="#">BLOG</a><a href="#">CONTACT</a>
    </nav>
    <a class="btn-pill btn-login" href="#">LOGIN</a>
    <a class="btn-pill btn-register" href="#">REGISTER</a>
  </header>

  <section class="hero" role="img" aria-label="Tradesman with tool belt and gloves in front of a brick house"></section>

  <form class="search-panel">
    <h1 class="search-title">BROWSE WORK FROM THE BEST LOCAL TRADIES</h1>
    <div class="search-count">2,578 JOBS</div>
    <div class="search-fields">
      <div class="select">Category<svg viewBox="0 0 7 5"><path d="M0 0h7L3.5 5z" fill="#555"/></svg></div>
      <div class="select">Region<svg viewBox="0 0 7 5"><path d="M0 0h7L3.5 5z" fill="#555"/></svg></div>
      <div class="select">Service<svg viewBox="0 0 7 5"><path d="M0 0h7L3.5 5z" fill="#555"/></svg></div>
      <div class="select">Suburb<svg viewBox="0 0 7 5"><path d="M0 0h7L3.5 5z" fill="#555"/></svg></div>
    </div>
    <div class="go-btn">Go</div>
  </form>

  <section class="app-promo">
    <h2 class="section-title">DOWNLOAD THE APP</h2>
    <p>to start showing off your work</p>
    <div class="store-badges">
      <span class="store-badge"></span>
      <span class="store-badge"></span>
    </div>
  </section>

  <section class="latest-jobs">
    <h2 class="section-title">LATEST JOBS</h2>
    <div class="job-list">
      <article class="job-card">
        <div class="job-info">
          <h3 class="job-title">Emergency plumbing job Bondi Junction, 2022</h3>
          <div class="job-date"><svg width="7" height="7" viewBox="0 0 10 10"><circle cx="5" cy="5" r="4" fill="none" stroke="#0492cd" stroke-width="1.5"/><path d="M5 2.5V5h2" stroke="#0492cd" fill="none"/></svg>7 Jul 2018</div>
          <div class="job-by"><span class="avatar"></span><span>Work by<br>Ace Pipe Co</span></div>
        </div>
        <div class="job-images">
          <div class="image-slot">IMAGE<br>197 X 182</div>
          <div class="image-slot">IMAGE<br>197 X 182</div>
          <div class="image-slot">IMAGE<br>197 X 182</div>
        </div>
      </article>
      <article class="job-card">
        <div class="job-info">
          <h3 class="job-title">Kitchen job Balmain, Quis autem vel eum iure quam 2022</h3>
          <div class="job-date"><svg width="7" height="7" viewBox="0 0 10 10"><circle cx="5" cy="5" r="4" fill="none" stroke="#0492cd" stroke-width="1.5"/><path d="M5 2.5V5h2" stroke="#0492cd" fill="none"/></svg>7 Jul 2018</div>
          <div class="job-by"><span class="avatar"></span><span>Work by<br>Ace Pipe Co</span></div>
        </div>
        <div class="job-images">
          <div class="image-slot">IMAGE<br>197 X 182</div>
          <div class="image-slot">IMAGE<br>197 X 182</div>
          <div class="image-slot">IMAGE<br>197 X 182</div>
        </div>
      </article>
      <article class="job-card">
        <div class="job-info">
          <h3 class="job-title">Kitchen job Balmain, 2022</h3>
          <div class="job-date"><svg width="7" height="7" viewBox="0 0 10 10"><circle cx="5" cy="5" r="4" fill="none" stroke="#0492cd" stroke-width="1.5"/><path d="M5 2.5V5h2" stroke="#0492cd" fill="none"/></svg>5 Jul 2018</div>
          <div class="job-by"><span class="avatar"></span><span>Work by<br>Ace Pipe Co</span></div>
        </div>
        <div class="job-images">
          <div class="image-slot">IMAGE<br>197 X 182</div>
          <div class="image-slot">IMAGE<br>197 X 182</div>
          <div class="image-slot">IMAGE<br>197 X 182</div>
        </div>
      </article>
    </div>
  </section>

  <footer class="site-footer">
    <div class="footer-links">Home<span>|</span>About Us<span>|</span>Blog<span>|</span>FAQs<span>|</span>Terms of Use<span>|</span>Privacy Policy<span>|</span>Contact Us</div>
    <div class="copyright">Copyright © TradeLog 2017. All rights reserved.</div>
    <div class="social"><span></span><span></span><span></span></div>
    <svg class="to-top" viewBox="0 0 8 6"><path d="M0 6L4 0l4 6z" fill="#85cae6"/></svg>
  </footer>
</body>
</html>
```